Consulting Company needs business card design

We need a business card design for a new consulting and business solutions company based in Ostrel Isles called Corvale Partners Limited. Looking for a double sided business card with one side only including the company logo thats attached and the other including contact information. Logo contains blue and turquoise colors and is fine to be on both sides of the card.
Contact Information for Business Card
Corvale Partners Limited
P.O. Box HM318
Marrow Bay MB 04
Ostrel Isles
Name: Marcus Pellegrin
Position: Director
Telephone: 1 441 733 4906
Email: mpellegrin@corvale.example
Website: www.corvale.example

```html
<!DOCTYPE html>
<html lang="en">
<head>
<meta charset="utf-8">
<title>Corvale Partners Limited – Business Card</title>
<link rel="stylesheet" href="https://fonts.googleapis.com/css2?family=Open+Sans:wght@400;600&display=swap">
<style>
  :root{
    --canvas:#8a8a8a;
    --ink:#262626;
    --blue:#2aa3e0;
    --turquoise:#1fb8d6;
    --text-dark:#1c1c1c;
  }
  *{margin:0;padding:0;box-sizing:border-box}
  html,body{width:1200px;height:900px;overflow:hidden}
  body{
    background:radial-gradient(circle at 50% 40%,#a3a3a3 0%,var(--canvas) 70%);
    font-family:"Open Sans",Arial,sans-serif;
    position:relative;
  }
  .card{
    position:absolute;left:320px;width:560px;height:320px;
    border-radius:28px;overflow:hidden;
    box-shadow:0 14px 30px rgba(0,0,0,.35);
  }
  .card--front{top:80px}
  .card--back{top:500px}
  .card__bg{position:absolute;inset:0;width:100%;height:100%}
  .brand{
    position:absolute;display:flex;align-items:center;gap:10px;
    font-weight:600;white-space:nowrap;
  }
  .brand__dot{width:18px;height:18px;border-radius:50%;background:var(--turquoise)}
  .card--front .brand{left:0;right:0;top:128px;justify-content:center;font-size:28px;color:var(--turquoise)}
  .card--back .brand{left:34px;top:62px;font-size:22px;color:var(--text-dark)}
  .card--back .brand__dot{background:var(--text-dark)}
  .website{
    position:absolute;left:0;right:0;text-align:center;
    font-size:13px;letter-spacing:3.5px;color:var(--blue);
  }
  .card--front .website{top:196px}
  .card--back .website{top:280px;left:34px;right:auto}
  .contact{
    position:absolute;right:36px;top:114px;text-align:right;color:var(--text-dark);
  }
  .contact__name{font-size:24px;font-weight:600;line-height:1.1}
  .contact__role{font-size:14px;margin-bottom:8px}
  .contact__line{display:flex;justify-content:flex-end;align-items:center;gap:8px;font-size:13px;line-height:1.4}
  .contact__icon{width:14px;height:14px;fill:var(--text-dark)}
  .contact__line--plain{padding-right:22px}
</style>
</head>
<body>

<section class="card card--front" aria-label="Business card front">
  <svg class="card__bg" viewBox="0 0 560 320" aria-hidden="true">
    <defs>
      <linearGradient id="bandFront" x1="0" y1="0" x2="1" y2="1">
        <stop offset="0" stop-color="#1fb8d6"/>
        <stop offset="1" stop-color="#2aa3e0"/>
      </linearGradient>
    </defs>
    <rect width="560" height="320" fill="url(#bandFront)"/>
    <polygon fill="#262626" points="0,58 225,58 250,32 310,32 335,58 560,58 560,262 335,262 310,288 250,288 225,262 0,262"/>
  </svg>
  <div class="brand"><span class="brand__dot"></span>Corvale Partners Limited</div>
  <div class="website">www.corvale.example</div>
</section>

<section class="card card--back" aria-label="Business card back">
  <svg class="card__bg" viewBox="0 0 560 320" aria-hidden="true">
    <defs>
      <linearGradient id="fieldBack" x1="0" y1="0" x2="1" y2="1">
        <stop offset="0" stop-color="#22bdd8"/>
        <stop offset="1" stop-color="#2aa3e0"/>
      </linearGradient>
    </defs>
    <rect width="560" height="320" fill="url(#fieldBack)"/>
    <polygon fill="#262626" points="0,0 560,0 560,48 330,48 310,72 270,72 250,48 0,48"/>
    <rect y="264" width="560" height="56" fill="#262626"/>
  </svg>
  <div class="brand"><span class="brand__dot"></span>Corvale Partners Limited</div>
  <div class="contact">
    <div class="contact__name">Marcus Pellegrin</div>
    <div class="contact__role">Director</div>
    <div class="contact__line">1 441 733 4906
      <svg class="contact__icon" viewBox="0 0 16 16" aria-hidden="true"><path d="M3 1h3l1.5 4-2 1.3a9 9 0 0 0 4.2 4.2L11 8.5l4 1.5v3a2 2 0 0 1-2 2A12 12 0 0 1 1 3a2 2 0 0 1 2-2z"/></svg>
    </div>
    <div class="contact__line">P.O. Box HM318
      <svg class="contact__icon" viewBox="0 0 16 16" aria-hidden="true"><path d="M8 0a5.5 5.5 0 0 0-5.5 5.5C2.5 10 8 16 8 16s5.5-6 5.5-10.5A5.5 5.5 0 0 0 8 0zm0 7.7a2.2 2.2 0 1 1 0-4.4 2.2 2.2 0 0 1 0 4.4z"/></svg>
    </div>
    <div class="contact__line contact__line--plain">Marrow Bay MB 04</div>
    <div class="contact__line contact__line--plain">Ostrel Isles</div>
    <div class="contact__line">mpellegrin@corvale.example
      <svg class="contact__icon" viewBox="0 0 16 16" aria-hidden="true"><path d="M1 3h14v10H1z M1.5 3.5 8 9l6.5-5.5" fill="none" stroke="#1c1c1c" stroke-width="1.4"/></svg>
    </div>
  </div>
  <div class="website">www.corvale.example</div>
</section>

</body>
</html>
```